The Velvet Needle Poster for a shop Facade

Hello Designers,

• We have a 4X4 meters façade for our tailor shop “The Velvet Needle”, and we are looking for a unique, simple and attractive poster to be printed on the glass to attract the attention of the driving customers or whoever passes by the shop.
• The Velvet Needle, with ‘Velvet’ referring to door-to-door service, our concept as follows (Call … Measure … Stitch … Deliver)

1. Step1: Book online or simply call us to make your appointment (should be pictorial not writing)
2. Step2: Our dedicated personnel will come to you at your preferred time and location. (should be pictorial not writing)
3. Step3: Clothes Alteration/Making to suit your style and body fit. (should be pictorial not writing)
4. Step4: Delivery on completion, at your preferred time and location. (should be pictorial not writing)

• We are specialized in clothes alteration and making for both men and women, and anything related to tailoring services www.thevelvetneedle.example

• The poster must include the name “The Velvet Needle” as well as the phone number 04 318 2976 in a very clear and obvious way (logo will be optional if you can show it in a nice way)
And the concept of our shop should be shown in the poster in a very simple and clear way and more graphical than words. (Perhaps a graphical flow to show client booking our service and we go to their place for alterations done).
Colors should be chosen carefully to attract the customers and the walk-ins eyes when they pass by either walking or by cars.

Thank you
Omar

Target Market(s)

We have a 4X4 meters façade for our tailor shop “The Velvet Needle”, and we are looking for a unique, simple and attractive poster to be printed on the glass to attract the attention of the driving customers or whoever passes by the shop.

Industry/Entity Type

Fashion

• to match the poster/signage

Colors

Designer to choose colors to be used in the design.

Requirements
Must have
Nice to have
• the concept of our shop should be shown in the poster in a very simple and clear way and more graphical than words. (Perhaps a graphical flow to show client booking our service and we go to their place for alterations done).
Should not have
• many words, copied designs. Please only use the images attached in the project brief for reference.

```html
<!DOCTYPE html>
<html lang="en">
<head>
<meta charset="utf-8">
<title>The Velvet Needle – Facade Poster</title>
<link rel="stylesheet" href="https://fonts.googleapis.com/css2?family=Arimo:wght@400;700&family=Zilla+Slab:ital,wght@0,700;1,700&display=swap">
<style>
  :root {
    --page: #ffffff;
    --frame: #2a2a2a;
    --teal: #1f3b42;
    --red-deep: #b71c1c;
    --red-bright: #ff5722;
    --red-fold: #7a1a1a;
    --orange: #ff7f00;
    --orange-light: #fdd57a;
    --orange-shade: #d96a00;
    --ink: #222222;
    --white: #ffffff;
    --cream: #fbe7c6;
  }
  * { margin: 0; padding: 0; box-sizing: border-box; }
  html, body { width: 1165px; height: 1200px; overflow: hidden; background: var(--page); }
  .canvas { width: 1165px; height: 1200px; position: relative; overflow: hidden; border: 1px solid var(--frame); }
  .stage { position: absolute; left: 0; top: 0; width: 1902px; height: 1960px; transform: scale(0.6125); transform-origin: 0 0; }
  .poster { position: absolute; left: 199px; top: 228px; width: 1503px; height: 1502px; background: var(--teal); }
  .poster-pattern { position: absolute; inset: 0; background: var(--teal); }
  .shapes { position: absolute; left: 0; top: 0; width: 1902px; height: 1960px; }
  .abs { position: absolute; white-space: nowrap; line-height: 1; }
  .site-url { left: 900px; top: 352px; font: 400 23px "Arimo", sans-serif; letter-spacing: 6.5px; color: var(--white); }
  .brand-mark { position: absolute; left: 1385px; top: 295px; width: 250px; height: 250px; border: 1.5px solid var(--white); border-radius: 50%;
    display: flex; flex-direction: column; align-items: center; justify-content: center; color: var(--white);
    font: 400 32px "Arimo", sans-serif; line-height: 1.15; text-align: center; }
  .brand-tagline { left: 1408px; top: 538px; width: 200px; text-align: center; font: 400 16px "Arimo", sans-serif; letter-spacing: 5px; line-height: 1.25; color: var(--white); white-space: normal; }
  .title-the { left: 786px; top: 394px; transform: translateX(-50%); font: 400 50px "Arimo", sans-serif; color: var(--white); }
  .title-name { left: 786px; top: 440px; transform: translateX(-50%); font: 700 98px "Zilla Slab", serif; color: var(--white); letter-spacing: 1px; }
  .call-line { left: 428px; top: 552px; color: var(--white); display: flex; align-items: baseline; gap: 18px; }
  .call-label { font: 400 37px "Arimo", sans-serif; }
  .call-number { font: 700 88px "Zilla Slab", serif; letter-spacing: 3px; font-variant-numeric: lining-nums; }
  .step-head { font: italic 700 132px "Zilla Slab", serif; color: var(--white); letter-spacing: 5px; }
  .step-text { font: 400 24px "Arimo", sans-serif; color: var(--ink); line-height: 1.25; }
  .art { position: absolute; border-radius: 10px; }
</style>
</head>
<body>
<div class="canvas">
  <div class="stage">
    <div class="poster">
      <div class="poster-pattern" role="img" aria-label="Faint pattern of sewing machines, buttons, pins, spools and scissors"></div>
    </div>

    <svg class="shapes" viewBox="0 0 1902 1960" aria-hidden="true">
      <defs>
        <linearGradient id="ribbonFill" x1="0" y1="0" x2="1" y2="0">
          <stop offset="0" stop-color="#b71c1c"/>
          <stop offset="0.35" stop-color="#c42020"/>
          <stop offset="1" stop-color="#ff5722"/>
        </linearGradient>
        <linearGradient id="panelFill" x1="0.45" y1="0.3" x2="1" y2="1">
          <stop offset="0" stop-color="#ff7f00"/>
          <stop offset="1" stop-color="#fdd57a"/>
        </linearGradient>
      </defs>
      <path d="M290 640 L415 655 L405 732 Q310 722 282 690 Z" fill="#7a1a1a"/>
      <polygon points="413,660 1190,704 1225,598 1630,598 1478,1646 270,1646" fill="url(#panelFill)"/>
      <polygon points="430,660 1190,704 1225,598 1270,598 1245,630 1190,700" fill="#d96a00" opacity="0.7"/>
      <path d="M295 383 L1357 383 L1183 657 L290 657 Q275 657 275 640 L275 400 Q275 383 295 383 Z" fill="url(#ribbonFill)"/>
      <g class="phone-icon" fill="#222222">
        <path d="M700 770 q-30 10 -36 40 q4 40 40 70 q30 25 60 22 q25 -6 32 -26 l-30 -30 q-12 14 -24 8 q-24 -16 -36 -40 q-4 -12 10 -20 z"/>
        <path d="M755 760 q40 20 45 70" fill="none" stroke="#222222" stroke-width="7" stroke-linecap="round"/>
        <path d="M752 785 q22 12 25 40" fill="none" stroke="#222222" stroke-width="5" stroke-linecap="round"/>
      </g>
    </svg>

    <div class="art" style="left:470px;top:955px;width:142px;height:205px;background:var(--cream);" role="img" aria-label="Illustration of a coiled measuring tape"></div>
    <div class="art" style="left:520px;top:1220px;width:228px;height:140px;background:var(--cream);" role="img" aria-label="Illustration of a sewing machine on a table with drawers"></div>
    <div class="art" style="left:388px;top:1435px;width:234px;height:170px;background:var(--cream);" role="img" aria-label="Illustration of trousers and a checked shirt"></div>

    <div class="abs site-url">www.thevelvetneedle.example</div>
    <div class="brand-mark"><span>the</span><span>Velvet Needle</span></div>
    <div class="abs brand-tagline">Clothes Alterations</div>

    <div class="abs title-the">THE</div>
    <div class="abs title-name">VELVET NEEDLE</div>
    <div class="abs call-line"><span class="call-label">Call Us at:</span><span class="call-number">04 318 2976</span></div>

    <div class="abs step-head" style="left:878px;top:742px;">CALL...</div>
    <div class="abs step-text" style="left:878px;top:886px;">Book online or simply call us to make your appointment.</div>

    <div class="abs step-head" style="left:678px;top:958px;">MEASURE...</div>
    <div class="abs step-text" style="left:676px;top:1102px;">Our dedicated personnel will come to you at your preferred<br>time and location.</div>

    <div class="abs step-head" style="left:818px;top:1202px;">STITCH...</div>
    <div class="abs step-text" style="left:816px;top:1345px;">Clothes Alteration/Making to suit your style and body fit.</div>

    <div class="abs step-head" style="left:690px;top:1416px;">DELIVER...</div>
    <div class="abs step-text" style="left:690px;top:1560px;">Delivery on completion, at your preferred time and location.</div>
  </div>
</div>
</body>
</html>
```